Lawn mowing business card design

We need a business card design for our lawn mowing and gardening business which is located in the Northern Beaches of Sydney. Our business name is Meadowline Turf and our logo is predominantly green and yellow in color. Please see our website at www.meadowlineturf.com.au for design ideas. The business targets young professionals and older clientele. As such the font should be easy to read, but I also want the business card to be colorful and stand out.

Target Market(s)

young professionals

Industry/Entity Type

Lawn Care

Contact Information for Business Card

Meadowline Turf, Gareth Pellow, 0478559201, www.meadowlineturf.com.au, email: meadowlineturf@mailbox-example.com

Font styles to use
Serif

Colors
9bcb3b
fbed22

Requirements
Must have
• Must include the details listed above. Must include the attached logo.
Nice to have
• Logo attached with two copies. The logo without any writing is high quality, please feel free to be creative with the text stating our business name "Meadowline Turf" using this file.

```html
<!DOCTYPE html>
<html lang="en">
<head>
<meta charset="utf-8">
<title>Meadowline Turf — Business Card</title>
<link rel="stylesheet" href="https://fonts.googleapis.com/css2?family=Alegreya:wght@400;500&display=swap">
<style>
  :root {
    --backdrop: #dcdcdc;
    --card: #f7f7f5;
    --ink-green: #1f5f2c;
    --leaf: #5db53a;
    --leaf-dark: #2f6b27;
    --sun: #fbed22;
  }
  * { margin: 0; padding: 0; box-sizing: border-box; }
  html, body { width: 1200px; height: 900px; overflow: hidden; }
  body {
    background: var(--backdrop);
    font-family: "Alegreya", Georgia, serif;
    position: relative;
  }
  .card {
    position: absolute;
    width: 520px;
    height: 300px;
    background: var(--card);
    box-shadow: 0 10px 24px rgba(0,0,0,0.12);
    overflow: hidden;
  }
  .card--back { left: 70px; top: 450px; }
  .card--front { left: 610px; top: 160px; }
  .swoosh { position: absolute; left: 0; bottom: 0; width: 100%; height: 100%; }

  .brand {
    position: absolute;
    display: flex;
    align-items: center;
    gap: 10px;
    color: var(--ink-green);
    font-weight: 500;
    white-space: nowrap;
  }
  .brand__dot {
    width: 16px; height: 16px;
    border-radius: 50%;
    background: var(--sun);
    flex: none;
  }
  .card--back .brand { left: 50%; top: 92px; transform: translateX(-50%); font-size: 30px; }
  .card--front .brand { right: 34px; top: 118px; font-size: 21px; }

  .identity { position: absolute; left: 54px; top: 52px; color: var(--ink-green); line-height: 1.1; }
  .identity__company { font-size: 21px; font-weight: 500; }
  .identity__person { font-size: 18px; }

  .contact { position: absolute; left: 42px; top: 122px; list-style: none; color: var(--ink-green); font-size: 14px; }
  .contact__item { display: flex; align-items: center; gap: 10px; height: 22px; }
  .contact__icon { width: 14px; height: 14px; flex: none; }
</style>
</head>
<body>

<section class="card card--back" aria-label="Card back">
  <div class="brand"><span class="brand__dot"></span>Meadowline Turf</div>
  <svg class="swoosh" viewBox="0 0 520 300" preserveAspectRatio="none" aria-hidden="true">
    <path d="M0 208 C150 236 320 250 520 256 L520 300 L0 300 Z" fill="var(--leaf-dark)"/>
    <path d="M0 214 C150 242 320 256 520 262 L520 300 L0 300 Z" fill="var(--leaf)"/>
    <path d="M0 238 C170 268 340 278 520 300 L0 300 Z" fill="var(--card)"/>
  </svg>
</section>

<section class="card card--front" aria-label="Card front">
  <div class="identity">
    <p class="identity__company">Meadowline Turf</p>
    <p class="identity__person">Gareth Pellow</p>
  </div>
  <ul class="contact">
    <li class="contact__item">
      <svg class="contact__icon" viewBox="0 0 16 16" aria-hidden="true"><path d="M4 1 L6.5 4.5 L5 6.5 C6 8.5 7.5 10 9.5 11 L11.5 9.5 L15 12 L13 15 C7 14 2 9 1 3 Z" fill="var(--ink-green)"/></svg>
      <span>0478559201</span>
    </li>
    <li class="contact__item">
      <svg class="contact__icon" viewBox="0 0 16 16" aria-hidden="true"><rect x="1" y="3" width="14" height="10" fill="var(--ink-green)"/><path d="M1.5 3.5 L8 9 L14.5 3.5" stroke="var(--card)" stroke-width="1.3" fill="none"/></svg>
      <span>meadowlineturf@mailbox-example.com</span>
    </li>
    <li class="contact__item">
      <svg class="contact__icon" viewBox="0 0 16 16" aria-hidden="true"><circle cx="8" cy="8" r="7" fill="none" stroke="var(--ink-green)" stroke-width="1.4"/><ellipse cx="8" cy="8" rx="3" ry="7" fill="none" stroke="var(--ink-green)" stroke-width="1.2"/><path d="M1 8 H15" stroke="var(--ink-green)" stroke-width="1.2"/></svg>
      <span>www.meadowlineturf.com.au</span>
    </li>
  </ul>
  <div class="brand"><span class="brand__dot"></span>Meadowline Turf</div>
  <svg class="swoosh" viewBox="0 0 520 300" preserveAspectRatio="none" aria-hidden="true">
    <path d="M0 222 C120 222 230 250 320 300 L0 300 Z" fill="var(--leaf-dark)"/>
    <path d="M0 232 C120 232 240 262 320 300 L0 300 Z" fill="var(--leaf)"/>
  </svg>
</section>

</body>
</html>
```